Realistic/Photoshop creating : Stormgrid Ledger

Need a realistic image created /designed
I'm looking for an photoshop artist to create an image of a bible in the aesthetic of techwear. The tech in techwear stands for technical rather than technology. Ideally, I would like the image just to be front facing and a realistic bible with the same aesthetic. IE straps, webbing, matte black,water proof looking.
I've provided some more images below to give you an idea of what I'm looking for, something more tactical https://img2.pixvaultcdn.example/photos/r4/QX7hm2pLwe9TnaVbkcD3RgZy_K5.SS2 https://img1.pixvaultcdn.example/photos/r1/518204637/QX82kLmbvTqWpeHdNcY55zfRa_!!518204637.jpg https://img1.pixvaultcdn.example/photos/r3/903146825/QX5MnRtw_H7DgPs4VeLLqoaZa_!!903146825.jpg https://img1.pixvaultcdn.example/photos/r3/903146825/QX6JdW8sPEZvqMhr2YbLLLoeKa_!!903146825.jpg https://img3.pixvaultcdn.example/photos/r1/QX4.vRtmH3PeLdk7GbQosWna_K5.SS2 https://img4.pixvaultcdn.example/photos/r4/903146825/QX9GT3hw71zkPmLNRVVbeqYa_!!903146825.jpg
on the book it would say "Stormgrid Ledger"

```html
<!DOCTYPE html>
<html lang="en">
<head>
<meta charset="utf-8">
<title>Stormgrid Ledger — Cover</title>
<link rel="stylesheet" href="https://fonts.googleapis.com/css2?family=Bebas+Neue&display=swap">
<style>
  :root {
    --backdrop: #e4e4e4;
    --leather-hi: #2a2a2a;
    --leather-lo: #070707;
    --fabric: #1d1d1f;
    --fabric-line: #2b2b2e;
    --strap: #18181a;
    --strap-edge: #2e2e31;
    --stitch: #4a4a4e;
    --pinstripe: #5a1a22;
    --hardware: #0c0c0d;
    --gold-hi: #f2c84b;
    --gold-lo: #a9761a;
    --silver: #d8d8da;
    --zip-pull: #e8e2d6;
  }
  * { margin: 0; padding: 0; box-sizing: border-box; }
  html, body {
    width: 1200px; height: 874px; overflow: hidden;
    background: var(--backdrop);
  }
  .canvas { position: relative; width: 1200px; height: 874px; }
  .cover {
    position: absolute; left: 320px; top: 47px;
    width: 560px; height: 780px; overflow: hidden;
    background: radial-gradient(ellipse at 50% 40%, var(--leather-hi) 0%, var(--leather-lo) 70%);
    box-shadow: 0 18px 40px rgba(0,0,0,.25);
  }
  .fabric-panel {
    position: absolute; left: 0; right: 0; top: 480px; bottom: 0;
    background:
      repeating-linear-gradient(0deg, var(--fabric-line) 0 1px, transparent 1px 4px),
      var(--fabric);
    border-top: 2px solid #2a2a2d;
    box-shadow: inset 0 8px 14px rgba(0,0,0,.6);
  }
  .pocket-flap {
    position: absolute; left: 170px; right: 170px; top: 565px; height: 40px;
    border: 1px dashed var(--stitch); border-top: none;
  }
  .pinstripe {
    position: absolute; top: 480px; bottom: 0; width: 2px;
    background: var(--pinstripe);
  }
  .pinstripe--left { left: 232px; }
  .pinstripe--right { left: 326px; }
  .strap {
    position: absolute; top: 0; bottom: 0; width: 56px;
    background: linear-gradient(90deg, var(--strap-edge), var(--strap) 20%, var(--strap) 80%, var(--strap-edge));
  }
  .strap::before, .strap::after {
    content: ""; position: absolute; top: 0; bottom: 0; width: 0;
    border-left: 1px dashed var(--stitch);
  }
  .strap::before { left: 5px; }
  .strap::after { right: 5px; }
  .strap--left { left: 150px; }
  .strap--right { left: 354px; }
  .strap-clip {
    position: absolute; width: 76px; height: 150px; top: 385px;
    background: linear-gradient(180deg, #1a1a1c, var(--hardware));
    border-radius: 38px 38px 10px 10px;
  }
  .strap-clip--left { left: 140px; }
  .strap-clip--right { left: 344px; }
  .zip-pull {
    position: absolute; left: 250px; top: 590px; width: 60px; height: 120px;
    background: linear-gradient(180deg, var(--zip-pull) 0%, #b8924a 60%, #6a5226 100%);
    border-radius: 30px 30px 6px 6px;
  }
  .corner {
    position: absolute; top: 0; width: 80px; height: 80px;
    background: linear-gradient(135deg, var(--gold-hi), var(--gold-lo));
  }
  .corner--left { left: 0; clip-path: polygon(0 0, 100% 0, 0 100%); }
  .corner--right { right: 0; clip-path: polygon(0 0, 100% 0, 100% 100%); }
  .title {
    position: absolute; left: 0; right: 0; top: 195px;
    text-align: center; color: var(--silver);
    font-family: "Bebas Neue", sans-serif; line-height: .86;
  }
  .title__top { display: block; font-size: 64px; letter-spacing: 1px; }
  .title__bottom { display: block; font-size: 118px; }
</style>
</head>
<body>
  <main class="canvas">
    <section class="cover" aria-label="Stormgrid Ledger book cover">
      <div class="fabric-panel"></div>
      <div class="pinstripe pinstripe--left"></div>
      <div class="pinstripe pinstripe--right"></div>
      <div class="pocket-flap"></div>
      <div class="strap strap--left"></div>
      <div class="strap strap--right"></div>
      <div class="strap-clip strap-clip--left" role="img" aria-label="Black metal ring and swivel clip on the left strap"></div>
      <div class="strap-clip strap-clip--right" role="img" aria-label="Black metal ring and swivel clip on the right strap"></div>
      <div class="zip-pull" role="img" aria-label="Cream D-ring zipper pull with brass zipper teeth"></div>
      <div class="corner corner--left" role="img" aria-label="Gold filigree corner ornament"></div>
      <div class="corner corner--right" role="img" aria-label="Gold filigree corner ornament"></div>
      <h1 class="title">
        <span class="title__top">Stormgrid</span>
        <span class="title__bottom">Ledger</span>
      </h1>
    </section>
  </main>
</body>
</html>
```